Business Card Design for sports performance / psychology company

You can see my website that this is based upon here:
http://www.trelvoxcoaching.co.uk

More than happy to answer any additional questions that you might have

** Happy for any images from Pixelgrove to be used. If I go with your design I will purchase the image for you to use

Target Market(s)

Football players

Industry/Entity Type

Business

Contact Information for Business Card

Name: Dewi Ansell
Title: Clinical Hypnotherapist & Strategist
Email address: dewi@trelvoxcoaching.co.uk
Tel: 07481926657

Font styles to use
Other font styles liked:
• Same font as on website. I'm not actually sure what it is

Requirements
Must have
• Tagline:
• Focus x Belief = Consistency
• Train the mind for every match
Nice to have
• Happy for designers to be creative
Should not have

```html
<!DOCTYPE html>
<html lang="en">
<head>
<meta charset="utf-8">
<title>Trelvox Coaching – Business Card</title>
<link href="https://fonts.googleapis.com/css2?family=Montserrat:wght@400;500;600&display=swap" rel="stylesheet">
<style>
  :root {
    --ink: #2a2352;
    --ink-soft: #55536a;
    --paper: #ffffff;
    --backdrop: #dcdce2;
    --night-top: #3b3466;
    --night-bottom: #221c43;
    --on-night: #ffffff;
  }
  * { margin: 0; padding: 0; box-sizing: border-box; }
  html, body { width: 1200px; height: 720px; overflow: hidden; }
  body {
    background: var(--backdrop);
    font-family: "Montserrat", sans-serif;
    position: relative;
  }
  .card {
    position: absolute;
    top: 223px;
    width: 465px;
    height: 266px;
  }
  .card--front { left: 125px; background: var(--paper); color: var(--ink); }
  .card--back {
    left: 608px;
    background: linear-gradient(160deg, var(--night-top) 0%, var(--night-bottom) 100%);
    color: var(--on-night);
  }
  .brand {
    position: absolute;
    display: flex;
    align-items: center;
    gap: 12px;
    font-weight: 500;
    text-transform: uppercase;
    letter-spacing: 0.01em;
    white-space: nowrap;
  }
  .brand__mark { display: block; background: currentColor; }
  .card--front .brand { left: 24px; top: 45px; font-size: 20px; }
  .card--front .brand__mark { width: 42px; height: 42px; }
  .card--back .brand { left: 72px; top: 102px; font-size: 23px; gap: 16px; }
  .card--back .brand__mark { width: 56px; height: 60px; background: var(--on-night); }

  .person { position: absolute; left: 78px; top: 124px; }
  .person__name { font-size: 14.5px; font-weight: 500; text-transform: uppercase; }
  .person__first { font-weight: 600; }
  .person__role { font-size: 11px; color: var(--ink-soft); margin-top: 3px; }

  .contacts { position: absolute; left: 78px; top: 180px; list-style: none; }
  .contacts li {
    display: flex; align-items: center; gap: 6px;
    font-size: 11px; color: var(--ink-soft); height: 17px;
  }
  .contacts svg { width: 12px; height: 12px; flex: none; fill: var(--ink); }
  .contacts strong { font-weight: 600; color: var(--ink); }

  .social { position: absolute; left: 326px; top: 216px; display: flex; gap: 8px; }
  .social span { width: 11px; height: 11px; background: var(--ink); display: block; }

  .tagline {
    position: absolute; left: 0; right: 0; top: 232px;
    text-align: center; font-size: 10.5px; letter-spacing: 0.01em;
  }
  .tagline__divider { margin: 0 6px; }
</style>
</head>
<body>
  <section class="card card--front" aria-label="Card front">
    <div class="brand"><span class="brand__mark"></span>Trelvox Coaching</div>
    <div class="person">
      <p class="person__name"><span class="person__first">Dewi</span> Ansell</p>
      <p class="person__role">Clinical Hypnotherapist &amp; Strategist</p>
    </div>
    <ul class="contacts">
      <li>
        <svg viewBox="0 0 12 12" aria-hidden="true"><path d="M1 4c0-2 2-3 5-3s5 1 5 3v1H8V4H4v1H1zM3 6h6l2 4H1z"/></svg>
        07481926657
      </li>
      <li>
        <svg viewBox="0 0 12 12" aria-hidden="true"><path d="M1 2.5h10v7H1z M1.5 3l4.5 3.5L10.5 3" fill="none" stroke="#2a2352" stroke-width="1.2"/></svg>
        dewi@trelvoxcoaching.co.uk
      </li>
      <li>
        <svg viewBox="0 0 12 12" aria-hidden="true"><circle cx="6" cy="6" r="4.8" fill="none" stroke="#2a2352" stroke-width="1.3"/><path d="M1.5 6h9M6 1.2c-2 3-2 6.6 0 9.6M6 1.2c2 3 2 6.6 0 9.6" fill="none" stroke="#2a2352" stroke-width="1"/></svg>
        <span>www.<strong>trelvoxcoaching</strong>.co.uk</span>
      </li>
    </ul>
    <div class="social" aria-label="Social profiles"><span></span><span></span><span></span></div>
  </section>

  <section class="card card--back" aria-label="Card back">
    <div class="brand"><span class="brand__mark"></span>Trelvox Coaching</div>
    <p class="tagline">Focus x Belief = Consistency<span class="tagline__divider">|</span>Train the mind for every match</p>
  </section>
</body>
</html>
```